Business card design needed

I am branching out into the world of private practice in Speech Pathology. My clients will be aged 0-17; the business card will be distributed within my existing teacher and parent networks in schools.

I work with clients to develop their speech, language, literacy, fluency, swallowing and voice. I like to think that parents hand over their money to me because I've offered a fun session with positive outcomes/growth and for an affordable price.

I'm flexible with colours; though think something bright would be ideal. I'm not wanting anything too cutesy or 'little kid'. I'd like for it to stand out in a bulging purse or on a fridge crammed with papers.

Industry/Entity Type

Teacher

Contact Information for Business Card

Wren Hollow Speech Pathology Pty Ltd
Molly Fenwick
Speech Pathologist
Ph: 0419 826 307
Email: mollyfenwick@quillpost.com

Logo Text

Logo styles of interest
Character Logo
Wordmark Logo
Lettermark Logo
Requirements
Must have
• A kind of graphic to represent the core business - that is, providing intervention to children 0-17 with communication needs (e.g., speech, language, literacy, swallowing, voice, fluency)

Should not have
• Pictures of babies or children.
Love hearts.

```html
<!DOCTYPE html>
<html lang="en">
<head>
<meta charset="utf-8">
<title>Wren Hollow Speech Pathology – Business Card</title>
<link rel="stylesheet" href="https://fonts.googleapis.com/css2?family=Noto+Sans:wght@400&display=swap">
<style>
  :root {
    --paper: #f6f0f1;
    --ink: #3b1519;
    --olive: #4f5519;
    --olive-light: #6e7a2c;
    --lime: #9fd33c;
  }
  html, body {
    margin: 0;
    padding: 0;
    overflow: hidden;
    background: var(--paper);
  }
  .card {
    position: relative;
    width: 1200px;
    height: 741px;
    background: var(--paper);
    font-family: "Noto Sans", sans-serif;
    color: var(--ink);
    overflow: hidden;
  }
  .card__ground {
    position: absolute;
    left: 0;
    top: 432px;
    width: 1200px;
    height: 309px;
    background: var(--olive);
  }
  .card__name {
    position: absolute;
    left: 214px;
    top: 152px;
    margin: 0;
    font-size: 30px;
    font-weight: 400;
    line-height: 1;
  }
  .card__details {
    position: absolute;
    left: 431px;
    top: 136px;
    margin: 0;
    font-size: 20px;
    line-height: 28.5px;
    font-style: normal;
  }
  .card__details span { display: block; }
  .card__company {
    position: absolute;
    left: 0;
    width: 1200px;
    top: 561px;
    margin: 0;
    text-align: center;
    font-size: 46px;
    font-weight: 400;
    line-height: 1;
    color: var(--lime);
  }
  .card__birds {
    position: absolute;
    left: 881px;
    top: 340px;
    width: 268px;
    height: 114px;
    border-radius: 50px 50px 20px 20px;
    background: linear-gradient(180deg, var(--olive-light), var(--olive));
  }
</style>
</head>
<body>
  <div class="card">
    <div class="card__ground"></div>
    <div class="card__birds" role="img" aria-label="Illustration of three small green birds standing in a row, one larger parent bird and two chicks"></div>
    <h1 class="card__name">Molly Fenwick</h1>
    <address class="card__details">
      <span>Speech Pathologist</span>
      <span>Ph: 0419 826 307</span>
      <span>Email: mollyfenwick@quillpost.com</span>
    </address>
    <p class="card__company">Wren Hollow Speech Pathology Pty Ltd</p>
  </div>
</body>
</html>
```